Letterhead for financial advisor-insurance agent firm

Our company, Marlowe Thistle Insurance & Investments, is an insurance (health, life, home, auto, etc) and investment brokerage offering a suite of options to meet client needs. We need letterhead that is professional and embodies strength, security and sophistication.

Industry/Entity Type

Investment

```html
<!DOCTYPE html>
<html lang="en">
<head>
<meta charset="utf-8">
<title>Marlowe Thistle Letterhead</title>
<link href="https://fonts.googleapis.com/css2?family=Cinzel:wght@500&family=Cormorant+Garamond:wght@700&family=Open+Sans:wght@400&display=swap" rel="stylesheet">
<style>
  :root {
    --navy: #2f3458;
    --ink: #2b2f4f;
    --slate: #6d7488;
    --footer-text: #c7cad9;
    --footer-icon: #8b90a8;
    --paper: #ffffff;
    --backdrop: #eef0f3;
    --edge: #d6d8de;
  }
  * { margin: 0; padding: 0; box-sizing: border-box; }
  html, body {
    width: 1200px;
    height: 1048px;
    overflow: hidden;
    background: var(--backdrop);
  }
  .letterhead {
    position: absolute;
    left: 220px;
    top: 32px;
    width: 760px;
    height: 984px;
    background: var(--paper);
    border: 1px solid var(--edge);
  }
  .brand {
    position: absolute;
    left: 70px;
    top: 52px;
    width: 260px;
    text-align: center;
  }
  .brand-square {
    display: block;
    width: 42px;
    height: 42px;
    margin: 0 auto 10px;
    border: 2px solid var(--navy);
  }
  .brand-name {
    font-family: "Cinzel", serif;
    font-weight: 500;
    font-size: 22px;
    letter-spacing: 0.5px;
    color: var(--ink);
    line-height: 1.1;
  }
  .brand-tagline {
    font-family: "Cinzel", serif;
    font-weight: 500;
    font-size: 8.5px;
    letter-spacing: 1px;
    color: var(--ink);
    margin-top: 3px;
  }
  .contact {
    position: absolute;
    right: 58px;
    top: 104px;
    text-align: left;
  }
  .contact-email {
    display: flex;
    align-items: center;
    gap: 8px;
    font-family: "Open Sans", sans-serif;
    font-size: 14px;
    color: var(--ink);
  }
  .contact-web {
    margin-top: 6px;
    font-family: "Cormorant Garamond", serif;
    font-weight: 700;
    font-size: 16px;
    letter-spacing: 1.6px;
    color: var(--ink);
  }
  .footer-band {
    position: absolute;
    left: 0;
    right: 0;
    bottom: 0;
    height: 92px;
    background: var(--navy);
    font-family: "Open Sans", sans-serif;
    font-size: 12px;
    color: var(--footer-text);
  }
  .footer-item {
    position: absolute;
    top: 30px;
    display: flex;
    align-items: center;
    gap: 10px;
  }
  .footer-address { left: 36px; }
  .footer-phone { left: 452px; top: 50px; }
  .footer-fax { left: 600px; top: 50px; }
  .footer-item svg { flex: none; }
</style>
</head>
<body>
  <main class="letterhead">
    <header class="brand">
      <span class="brand-square"></span>
      <div class="brand-name">Marlowe Thistle</div>
      <div class="brand-tagline">Insurance &amp; Investments</div>
    </header>

    <section class="contact">
      <div class="contact-email">
        <svg width="24" height="18" viewBox="0 0 24 18" aria-hidden="true">
          <rect x="1" y="1" width="22" height="16" rx="1.5" fill="var(--slate)"/>
          <path d="M1.5 2 L12 10 L22.5 2" fill="none" stroke="#fff" stroke-width="1.4"/>
        </svg>
        <span>info@marlowethistle.com</span>
      </div>
      <div class="contact-web">www.marlowethistle.com</div>
    </section>

    <footer class="footer-band">
      <div class="footer-item footer-address">
        <svg width="18" height="16" viewBox="0 0 18 16" aria-hidden="true">
          <path d="M9 1 L17 8 H14.5 V15 H11 V10.5 H7 V15 H3.5 V8 H1 Z" fill="var(--footer-icon)"/>
        </svg>
        <span>Marlowe Thistle Building, 2715 W. Harbor Blvd, Ste.</span>
      </div>
      <div class="footer-item footer-phone">
        <svg width="16" height="14" viewBox="0 0 16 14" aria-hidden="true">
          <path d="M1 4 Q8 0 15 4 L14 6 L11 5 L11 4 Q8 3 5 4 L5 5 L2 6 Z" fill="var(--footer-icon)"/>
          <rect x="3" y="7" width="10" height="6" rx="1" fill="var(--footer-icon)"/>
        </svg>
        <span>(456) 555-0182</span>
      </div>
      <div class="footer-item footer-fax">
        <svg width="16" height="14" viewBox="0 0 16 14" aria-hidden="true">
          <rect x="4" y="1" width="8" height="5" fill="none" stroke="var(--footer-icon)" stroke-width="1.3"/>
          <rect x="1" y="5" width="14" height="8" rx="1.5" fill="var(--footer-icon)"/>
        </svg>
        <span>(456) 555-0182</span>
      </div>
    </footer>
  </main>
</body>
</html>
```